Corvelle Strategies business card

I need a business card for my new strategic consulting LLC, Corvelle Strategies. We specialize in helping people who care about broadband technology and telecommunications policy, and we're based in Washington DC. I'm looking for a card that says smart, credible, future-facing and signals a high level of expertise. It's DC, so there's clearly a limit to how crazy we can go with this card, but I am looking for a design that reflects a company that is comfortable with technology, policy, and having a little bit fun. I'm uploading my logo below, and I'd like to have it be part of the card design in some fashion.
Target Market(s)
Telecommunications and technology policy professionals
Industry/Entity Type
Technology policy
Contact Information for Business Card
Name of business, my name (Glen Mosswater), email (glen@corvellestrategies-example.com) , phone number (202-555-0148)phone number

```html
<!DOCTYPE html>
<html lang="en">
<head>
<meta charset="utf-8">
<title>Corvelle Strategies – Business Card</title>
<link rel="stylesheet" href="https://fonts.googleapis.com/css2?family=Quicksand:wght@700&family=Open+Sans:wght@400;600&display=swap">
<style>
  :root {
    --stage: #c5cad5;
    --brand-blue: #0b56a0;
    --card-white: #ffffff;
    --accent-sun: #f5a623;
    --faint-grey: #eceef0;
    --shadow: rgba(0, 0, 0, 0.45);
  }
  * { box-sizing: border-box; margin: 0; padding: 0; }
  html, body { width: 1200px; height: 960px; overflow: hidden; }
  body {
    background: var(--stage);
    position: relative;
    font-family: "Open Sans", sans-serif;
  }
  .card {
    position: absolute;
    width: 661px;
    height: 376px;
    box-shadow: 6px 7px 6px var(--shadow);
    overflow: hidden;
  }
  .card--front { left: 275px; top: 92px; background: var(--card-white); }
  .card--back { left: 277px; top: 506px; background: var(--brand-blue); }

  .wordmark {
    position: absolute;
    display: flex;
    align-items: center;
    gap: 12px;
    font-family: "Quicksand", sans-serif;
    font-weight: 700;
    color: var(--brand-blue);
    white-space: nowrap;
  }
  .wordmark__dot {
    width: 26px; height: 26px;
    border-radius: 50%;
    background: var(--accent-sun);
    flex: none;
  }
  .card--front .wordmark {
    left: 0; right: 0; top: 68px;
    justify-content: center;
    font-size: 40px;
  }

  .backdrop-art {
    position: absolute;
    right: 0; bottom: 0;
    width: 260px; height: 230px;
    background: radial-gradient(ellipse at 75% 70%, var(--faint-grey) 0%, rgba(236,238,240,0.6) 45%, rgba(236,238,240,0) 75%);
  }

  .holder-name {
    position: absolute;
    left: 32px; top: 218px;
    font-family: "Quicksand", sans-serif;
    font-weight: 700;
    font-size: 39px;
    color: var(--brand-blue);
    letter-spacing: 0.2px;
  }
  .contact-list {
    position: absolute;
    left: 38px; top: 278px;
    list-style: none;
  }
  .contact-list li {
    display: flex;
    align-items: center;
    gap: 9px;
    height: 30px;
    font-size: 18px;
    color: var(--brand-blue);
  }
  .contact-list svg { width: 21px; height: 21px; flex: none; }

  .logo-plate {
    position: absolute;
    left: 151px; top: 138px;
    width: 358px; height: 82px;
    background: var(--card-white);
  }
  .card--back .wordmark {
    left: 0; right: 0; top: 0; bottom: 0;
    justify-content: center;
    gap: 10px;
    font-size: 29px;
  }
  .card--back .wordmark__dot { width: 20px; height: 20px; }
  .website {
    position: absolute;
    left: 0; right: 0; top: 250px;
    text-align: center;
    color: var(--card-white);
    font-weight: 600;
    font-size: 18px;
    letter-spacing: 0.6px;
  }
</style>
</head>
<body>
  <section class="card card--front" aria-label="Card front">
    <div class="backdrop-art" role="img" aria-label="Faint brand decoration area"></div>
    <div class="wordmark">Corvelle Strategies<span class="wordmark__dot"></span></div>
    <h1 class="holder-name">Glen Mosswater</h1>
    <ul class="contact-list">
      <li>
        <svg viewBox="0 0 20 20" aria-hidden="true">
          <rect x="0" y="0" width="20" height="20" rx="4" fill="var(--brand-blue)"/>
          <rect x="4" y="6" width="12" height="9" fill="none" stroke="#fff" stroke-width="1.5"/>
          <path d="M4 6 L10 11 L16 6" fill="none" stroke="#fff" stroke-width="1.5"/>
        </svg>
        glen@corvellestrategies-example.com
      </li>
      <li>
        <svg viewBox="0 0 20 20" aria-hidden="true">
          <rect x="0" y="0" width="20" height="20" rx="4" fill="var(--brand-blue)"/>
          <path d="M6 4 L8 4 L9 7.5 L7.6 8.6 C8.3 10.4 9.6 11.7 11.4 12.4 L12.5 11 L16 12 L16 14 C16 15 15 16 14 16 C9 15.5 4.5 11 4 6 C4 5 5 4 6 4 Z" fill="#fff"/>
        </svg>
        202-555-0148
      </li>
    </ul>
  </section>

  <section class="card card--back" aria-label="Card back">
    <div class="logo-plate">
      <div class="wordmark">Corvelle Strategies<span class="wordmark__dot"></span></div>
    </div>
    <p class="website">www.corvellestrategies-example.com</p>
  </section>
</body>
</html>
```